Spiritual Self Help Book Cover

I need a book cover that's extremely appealing to spiritual seekers, self-help/health and wellness fans. Mostly for women.
The book blends spirituality/mysticism with science for readers to understand how to optimize their health/body, emotional well-being, mental wellness, spiritual fulfillment, relationships, business and purpose in life. It infuses ancient and modern understanding of energy/frequency/quantum mechanics along with the science of chiropractic and psychology.
Book title: Folding Every Lantern Inward
I'll attach some examples that are similar to what I like but I want something different and more extravagantly beautiful.
Please use the graphic of the Sri Yantra Mandala into the cover instead of this stock image one.
I'll need the book cover in all formats: paperback, hardcover, ebook and audiobook.
I'll provide the rest of the details, including publisher logo, synopsis, author photo/blurb and ISBN after I pick the final wniner.
Mostly women spiritual seekers, self-help readers, health/wellness enthusiasts

```html
<!DOCTYPE html>
<html lang="en">
<head>
<meta charset="utf-8">
<title>Folding Every Lantern Inward — Book Cover</title>
<link rel="stylesheet" href="https://fonts.googleapis.com/css2?family=Big+Shoulders+Display:wght@700;800&family=Oswald:wght@500&display=swap">
<style>
  :root {
    --backdrop: #d3d8b0;
    --backdrop-edge: #b9c49a;
    --cover-violet: #3f2870;
    --geometry-violet: #4a3580;
    --gold-light: #d8c46a;
    --gold-mid: #c8a63e;
    --gold-deep: #b18a2a;
    --author-cream: #e4d9b6;
    --emblem-light: #d9ccb0;
    --emblem-deep: #bfae8c;
  }
  * { margin: 0; padding: 0; box-sizing: border-box; }
  html, body {
    width: 1200px;
    height: 937px;
    overflow: hidden;
  }
  body {
    background: radial-gradient(ellipse at 50% 30%, #dfe2bb 0%, var(--backdrop) 50%, var(--backdrop-edge) 100%);
    position: relative;
  }
  .book-cover {
    position: absolute;
    left: 350px;
    top: 68px;
    width: 500px;
    height: 800px;
    background: var(--cover-violet);
    overflow: hidden;
  }
  .sacred-geometry-area {
    position: absolute;
    left: 70px;
    top: 70px;
    width: 430px;
    height: 420px;
    background: radial-gradient(ellipse at 55% 50%, var(--geometry-violet) 0%, rgba(74, 53, 128, 0.45) 45%, rgba(63, 40, 112, 0) 72%);
  }
  .title-block {
    position: absolute;
    left: 95px;
    top: 150px;
    font-family: "Big Shoulders Display", sans-serif;
    font-weight: 800;
    font-size: 112px;
    text-transform: uppercase;
    line-height: 0.92;
    letter-spacing: 1px;
    white-space: nowrap;
  }
  .title-row {
    display: flex;
    align-items: center;
    gap: 26px;
  }
  .title-line {
    display: block;
    background: linear-gradient(180deg, var(--gold-light) 0%, var(--gold-mid) 55%, var(--gold-deep) 100%);
    -webkit-background-clip: text;
    background-clip: text;
    color: transparent;
  }
  .meditation-emblem {
    display: block;
    width: 56px;
    height: 74px;
    border-radius: 28px 28px 12px 12px;
    background: linear-gradient(180deg, var(--emblem-light) 0%, var(--emblem-deep) 100%);
    opacity: 0.9;
  }
  .author-name {
    position: absolute;
    left: 97px;
    top: 712px;
    font-family: "Oswald", sans-serif;
    font-weight: 500;
    font-size: 19px;
    letter-spacing: 0.5px;
    text-transform: uppercase;
    color: var(--author-cream);
  }
</style>
</head>
<body>
  <main class="book-cover">
    <div class="sacred-geometry-area" role="img" aria-label="Faint Sri Yantra sacred geometry mandala behind the title"></div>
    <h1 class="title-block">
      <span class="title-line">Folding</span>
      <span class="title-row">
        <span class="title-line">Every</span>
        <span class="meditation-emblem" role="img" aria-label="Small emblem of a meditating figure rising from lotus leaves"></span>
      </span>
      <span class="title-line">Lantern</span>
      <span class="title-line">Inward</span>
    </h1>
    <p class="author-name">Dr. Maren Holloway</p>
  </main>
</body>
</html>
```